Design Android App for Creating Estimates and Invoices

This project is to create a graphic design for an Android mobile app called Velmira Contractor App which is an app that will help contractors to quickly create professional estimates and invoices, accept payments, manage clients and projects and run their business smoothly.

Link to some designs I created myself, hoping to get even better design from you
https://pixtray.example/album/qRwoPe

This project is similar to
https://apps.storefrontia.example/details?id=com.bracklyapp.android.brackly
https://apps.storefrontia.example/details?id=com.zeltru.billnote

Check this Google Doc for more information. http://shrtn.example/8KqPmX1

Target Market(s)

Contractors, Home Improvement Professionals, Home Builders,

Industry/Entity Type

Residential Construction

Requirements
Must have
• Non-cluttered screen for Estimates, Enough white space between fields.
Nice to have
• Be different from the two example designs shown

```html
<!DOCTYPE html>
<html lang="en">
<head>
<meta charset="utf-8">
<title>Velmira Contractor App – Create Estimate flow</title>
<link href="https://fonts.googleapis.com/css2?family=Lato:wght@300;400;700;900&display=swap" rel="stylesheet">
<style>
:root{
  --blue:#3d5ca8;
  --blue-tab:#5a76b7;
  --green:#7dc42a;
  --orange:#f27a1a;
  --ink:#2f3238;
  --muted:#9aa0a8;
  --line:#cdd2d9;
  --canvas:#e8e9eb;
  --red:#e53935;
}
*{box-sizing:border-box;margin:0;padding:0}
html,body{width:1200px;height:3155px;overflow:hidden;background:var(--canvas)}
body{font-family:'Lato',sans-serif;color:var(--ink)}
.board{position:absolute;left:0;top:0;width:980px;height:2576px;transform:scale(1.22449);transform-origin:0 0}
.caption{position:absolute;text-align:center;color:var(--muted);font-weight:300;font-size:15px;width:300px}
.caption small{display:block;font-size:11px;line-height:15px;margin-top:2px}
svg.ic{display:inline-block;flex:none}

/* phone screen */
.phone{position:absolute;width:252px;background:#fff;overflow:hidden;box-shadow:0 1px 3px rgba(0,0,0,.08)}
.phone > *{position:absolute}
.hero{left:0;top:0;width:252px;height:184px;background:var(--blue)}
.status{left:0;top:0;width:252px;height:16px;display:flex;justify-content:flex-end;align-items:center;gap:3px;padding-right:6px;color:#fff;font-size:8.5px}
.appbar{left:0;top:26px;width:252px;height:20px;display:flex;align-items:center;justify-content:center;color:#fff;font-weight:700;font-size:10.5px}
.appbar .back{position:absolute;left:10px;top:3px}
.appbar .menu{position:absolute;right:12px;top:4px}
.stepper{left:0;top:62px;width:252px;display:flex;justify-content:center;gap:14px}
.dot{width:14px;height:14px;border-radius:50%;border:1.2px solid #fff;color:#fff;font-size:7.5px;display:flex;align-items:center;justify-content:center}
.dot.cur{background:#fff;color:var(--blue);font-weight:700}
.dot.done{background:var(--green);border-color:var(--green)}
.tab{left:40px;top:94px;width:172px;height:12px;background:var(--blue-tab);border-radius:4px 4px 0 0}
.card{left:9px;top:100px;width:234px;height:90px;background:#fff;border-radius:4px 4px 0 0}
.saved{right:17px;top:111px;color:var(--orange);font-weight:700;font-size:7px;letter-spacing:.2px;display:flex;align-items:center;gap:3px}
.title{left:0;top:134px;width:252px;height:18px;display:flex;justify-content:center;align-items:center;gap:5px;font-weight:700;font-size:16px;letter-spacing:.3px}

.sec,.field,.chk,.row,.sh,.para,.sigbox,.lbl{left:17px;width:218px}
.sec{height:12px;display:flex;align-items:center;gap:4px;font-weight:700;font-size:10px}
.sec .rule{flex:1;height:1.2px;background:var(--ink)}
.sec .thin{font-weight:400;font-size:8.5px}
.field{height:32px;border:1px solid var(--line);font-size:10.5px;padding:0 8px;display:flex;align-items:center}
.field.area{align-items:flex-start;padding-top:11px;height:83px}
.field .lab{position:absolute;left:5px;top:-6px;background:#fff;padding:0 3px;font-size:7.5px;color:var(--muted)}
.field .ph{color:#b3b8bf}
.field .chev{position:absolute;right:8px;top:12px}
.chk{height:12px;display:flex;align-items:center;gap:7px;font-size:8.5px}
.box{width:11px;height:11px;border:1px solid #c5cad2;background:#fff;display:flex;align-items:center;justify-content:center}
.box.on{border-color:var(--green)}
.chk.off{color:#9aa0a8}
.chk.off .box{background:#eceef1;border-color:#e0e3e7}
.btn{left:42px;width:168px;height:33px;border-radius:17px;background:var(--blue);color:#fff;font-weight:900;font-size:10px;letter-spacing:.3px;display:flex;align-items:center;justify-content:center;gap:6px}
.btn.go{background:var(--green)}
.addbtn{left:17px;width:64px;height:20px;border:1px solid var(--orange);border-radius:10px;color:var(--orange);font-size:7px;font-weight:900;display:flex;align-items:center;justify-content:center;gap:3px}
.lbl{height:12px;font-size:10px;display:flex;align-items:center}
.toggle{left:196px;width:39px;height:13px;border-radius:3px;font-size:6.5px;font-weight:900;display:flex;align-items:center;padding:0 3px}
.toggle.on{background:var(--green);color:#fff;justify-content:space-between}
.toggle.on::after{content:"";width:11px;height:9px;background:#fff;border-radius:2px}
.toggle.off{border:1px solid #ccd0d6;color:#c0c4ca;justify-content:space-between;flex-direction:row-reverse}
.toggle.off::after{content:"";width:11px;height:9px;background:#fff;border:1px solid #ccd0d6;border-radius:2px}
.pays{left:17px;display:flex;gap:3px}
.pay{width:26px;height:14px;border:1px solid #d3d7dd;background:#fff;font-size:5.5px;font-weight:700;color:var(--blue);display:flex;align-items:center;justify-content:center}
.photo{width:45px;height:45px}
.photo.a{background:linear-gradient(180deg,#9fb6cf 0%,#c9c6bd 45%,#6f8a58 100%)}
.photo.b{background:linear-gradient(180deg,#a9c3e0 0%,#e3d8c6 50%,#b99a7a 100%)}
.photo .x{position:absolute;right:-4px;bottom:-4px;width:10px;height:10px;border-radius:50%;background:#b8bcc2;border:1.5px solid #fff}
.addphoto{width:45px;height:45px;border:1px solid var(--line);display:flex;align-items:center;justify-content:center}

/* estimate summary */
.pen{right:17px}
.logo{left:98px;top:168px;width:56px;height:56px;border-radius:50%;background:#eef0f3;color:#b5b9bf;font-size:5.5px;font-weight:700;letter-spacing:.6px;display:flex;align-items:center;justify-content:center}
.ctr{left:0;width:252px;text-align:center;font-size:7px;line-height:10px}
.sh{height:15px;border-bottom:1.5px solid var(--blue);color:var(--blue);font-weight:700;font-size:8.5px;display:flex;align-items:center;gap:4px;padding-bottom:2px}
.sh .ic.last{margin-left:auto}
.row{height:12px;display:flex;justify-content:space-between;align-items:center;font-size:9px}
.row b{font-weight:700}
.row.sub{font-size:7.5px}
.row.ind{left:51px;width:184px}
.sep{left:17px;width:218px;height:1px;background:#d9dde2}
.sep.ind{left:51px;width:184px}
.para{font-size:8.5px;line-height:14px}
.sigbox{height:45px;background:#fdf1e6}

/* popup */
.shade-top{left:0;top:0;width:252px;height:184px;background:#1f2b47}
.shade-bot{left:0;top:184px;width:252px;height:295px;background:#3c3e43}
.dialog{left:8px;top:46px;width:235px;height:388px;background:#fff;border-radius:3px}
.dialog > *{position:absolute}
.dialog .close{left:221px;top:-4px;width:14px;height:14px;border-radius:50%;background:#c7cbd0;border:1.5px solid #fff}
.dialog .head{left:0;top:34px;width:235px;text-align:center;color:var(--orange);font-weight:900;font-size:13.5px;display:flex;justify-content:center;align-items:center;gap:4px}
.opt{left:0;width:235px;border-top:1px solid #e3e6ea;padding:0 8px 0 9px;display:flex;align-items:center;gap:8px;font-size:9px}
.opt .nm{flex:1;font-weight:700}
.opt .nm small{display:block;font-weight:400;font-size:7.5px;margin-top:4px}
.opt.last{border-bottom:1px solid #e3e6ea}

.swipe{position:absolute;left:413px;top:1940px;width:252px;height:48px;background:#fff;box-shadow:0 1px 3px rgba(0,0,0,.08);font-size:9px}
.swipe > *{position:absolute}
</style>
</head>
<body>
<svg width="0" height="0" style="position:absolute">
  <defs>
    <symbol id="tick" viewBox="0 0 10 10"><path d="M2 5.2l2 2 4-4.4" fill="none" stroke="currentColor" stroke-width="1.6"/></symbol>
    <symbol id="go" viewBox="0 0 10 10"><path d="M1 1l8 4-8 4 2-4z" fill="currentColor"/></symbol>
    <symbol id="back" viewBox="0 0 14 14"><path d="M13 7H2M7 2L2 7l5 5" fill="none" stroke="currentColor" stroke-width="1.4"/></symbol>
    <symbol id="kebab" viewBox="0 0 4 12"><circle cx="2" cy="1.5" r="1.2" fill="currentColor"/><circle cx="2" cy="6" r="1.2" fill="currentColor"/><circle cx="2" cy="10.5" r="1.2" fill="currentColor"/></symbol>
    <symbol id="trash" viewBox="0 0 10 12"><path d="M1 2.5h8M3.5 2.5V1h3v1.5M2 3.5h6l-.6 7.5H2.6z" fill="currentColor" stroke="currentColor" stroke-width=".8"/></symbol>
    <symbol id="pencil" viewBox="0 0 12 12"><path d="M2 10l.6-2.6 6-6 2 2-6 6zM1 11.5h10" fill="none" stroke="currentColor" stroke-width="1.3"/></symbol>
    <symbol id="person" viewBox="0 0 16 16"><circle cx="8" cy="4.5" r="3.6" fill="currentColor"/><path d="M1 16c0-4.5 3-7 7-7s7 2.5 7 7z" fill="currentColor"/></symbol>
    <symbol id="house" viewBox="0 0 16 16"><path d="M8 1L0.5 7.5h2.3V15h4v-4.5h2.4V15h4V7.5h2.3z" fill="currentColor"/></symbol>
    <symbol id="wallet" viewBox="0 0 16 14"><path d="M2 3l9-2.5.8 2.5z" fill="currentColor"/><rect x="0.5" y="3.5" width="15" height="10" rx="1" fill="currentColor"/></symbol>
    <symbol id="doc" viewBox="0 0 12 16"><path d="M0.5 0.5h7l4 4v11h-11z" fill="currentColor"/><path d="M3 7h6M3 9.5h6M3 12h6" stroke="#fff" stroke-width="1"/></symbol>
    <symbol id="eye" viewBox="0 0 18 16"><rect x="1" y="1" width="16" height="14" rx="2" fill="none" stroke="currentColor" stroke-width="1.6"/><circle cx="9" cy="8" r="3.5" fill="currentColor"/></symbol>
    <symbol id="chev" viewBox="0 0 10 6"><path d="M1 1l4 4 4-4" fill="none" stroke="currentColor" stroke-width="1.3"/></symbol>
    <symbol id="plus" viewBox="0 0 10 10"><path d="M5 0v10M0 5h10" stroke="currentColor" stroke-width="1.2"/></symbol>
    <symbol id="okcircle" viewBox="0 0 12 12"><circle cx="6" cy="6" r="6" fill="currentColor"/><path d="M3.2 6.2l2 2 3.6-4" fill="none" stroke="#fff" stroke-width="1.4"/></symbol>
    <symbol id="signal" viewBox="0 0 24 9"><path d="M0 1.5a9 9 0 0 1 10 0L5 8z" fill="currentColor"/><path d="M11 8l6-7v7z" fill="currentColor"/><rect x="19" y="0.5" width="4" height="8" rx=".6" fill="currentColor"/></symbol>
  </defs>
</svg>

<main class="board">

  <p class="caption" style="left:53px;top:56px">Step 01</p>
  <p class="caption" style="left:361px;top:56px">Step 02</p>
  <p class="caption" style="left:627px;top:139px">Popup Window<small>A user can select multiple items</small></p>
  <p class="caption" style="left:32px;top:1225px">Step 03</p>
  <p class="caption" style="left:340px;top:1225px">Step 04</p>
  <p class="caption" style="left:648px;top:1191px">Step 05<small>A user reviews the created estimate &amp; sends to the client. (If needed, a user can edit info.)</small></p>

  <!-- STEP 01 : CLIENT -->
  <section class="phone" style="left:77px;top:84px;height:1056px">
    <div class="hero"></div>
    <div class="status"><svg class="ic" width="24" height="9"><use href="#signal"/></svg>15:30</div>
    <div class="appbar">Create Estimate<svg class="ic menu" width="4" height="12"><use href="#kebab"/></svg></div>
    <div class="stepper"><span class="dot cur">1</span><span class="dot">2</span><span class="dot">3</span><span class="dot">4</span><span class="dot">5</span></div>
    <div class="tab"></div><div class="card"></div>
    <div class="saved"><svg class="ic" width="6" height="6" style="color:var(--orange)"><use href="#go"/></svg>SAVED CLIENTS</div>
    <h2 class="title"><svg class="ic" width="16" height="16"><use href="#person"/></svg>CLIENT</h2>

    <div class="sec" style="top:166px">Basic Information<span class="rule"></span></div>
    <div class="field" style="top:193px"><span class="lab">Name</span>Jon Merrow</div>
    <div class="field" style="top:242px"><span class="lab">Company Name</span>Pellwick Diner</div>
    <div class="chk" style="top:292px"><span class="box on"><svg class="ic" width="9" height="9" style="color:var(--green)"><use href="#tick"/></svg></span>Use company name as primary name</div>
    <div class="field" style="top:327px"><span class="lab">Email</span>info@pellwickdiner.example</div>
    <div class="field" style="top:376px"><span class="lab">Mobile Phone</span>555.201.3344</div>
    <div class="field" style="top:425px"><span class="lab">Company/Home Phone</span>555.310.7781</div>

    <div class="sec" style="top:484px">Billing Address<span class="rule"></span></div>
    <div class="field" style="top:510px"><span class="lab">Address 1</span>48 Alder Lane</div>
    <div class="field" style="top:559px"><span class="lab">Address 2</span></div>
    <div class="field" style="top:608px"><span class="lab">City</span>Brookvale</div>
    <div class="field" style="top:657px"><span class="lab">State/Province</span>TX</div>
    <div class="field" style="top:706px"><span class="lab">Zip/Postal Code</span>75999</div>

    <div class="sec" style="top:765px">Worksite/Shipping Address<span class="rule"></span></div>
    <div class="chk" style="top:788px"><span class="box on"><svg class="ic" width="9" height="9" style="color:var(--green)"><use href="#tick"/></svg></span>Same as the billing address</div>

    <div class="sec" style="top:827px">Private Note <span class="thin">(invisible for the client)</span><span class="rule"></span></div>
    <div class="field area" style="top:853px"><span class="lab">Private Note</span></div>
    <div class="chk" style="top:949px"><span class="box"></span>Save this client for future use</div>
    <div class="btn" style="top:990px"><svg class="ic" width="10" height="10"><use href="#go"/></svg>NEXT</div>
  </section>

  <!-- STEP 02 : ITEMS -->
  <section class="phone" style="left:385px;top:84px;height:1062px">
    <div class="hero"></div>
    <div class="status"><svg class="ic" width="24" height="9"><use href="#signal"/></svg>15:30</div>
    <div class="appbar"><svg class="ic back" width="14" height="14"><use href="#back"/></svg>Create Estimate<svg class="ic menu" width="4" height="12"><use href="#kebab"/></svg></div>
    <div class="stepper"><span class="dot done"><svg class="ic" width="10" height="10"><use href="#tick"/></svg></span><span class="dot cur">2</span><span class="dot">3</span><span class="dot">4</span><span class="dot">5</span></div>
    <div class="tab"></div><div class="card"></div>
    <div class="saved"><svg class="ic" width="6" height="6"><use href="#go"/></svg>SAVED ITEMS</div>
    <h2 class="title"><svg class="ic" width="17" height="17"><use href="#house"/></svg>ITEMS</h2>

    <div class="sec" style="top:166px">Item 1<span class="rule"></span><svg class="ic" width="8" height="10" style="color:#c5c9cf"><use href="#trash"/></svg></div>
    <div class="field" style="top:193px"><span class="lab">Item Name</span>Asphalt (per sqft)</div>
    <div class="field" style="top:242px;width:109px"><span class="lab">Unit Cost</span>$85.00</div>
    <div class="field" style="top:242px;left:125px;width:110px"><span class="lab">Quantity</span>10</div>
    <div class="field area" style="top:290px"><span class="lab">Additional Details</span>including labour costs</div>
    <div class="chk off" style="top:386px"><span class="box"></span>Save this item for future use</div>

    <div class="sec" style="top:425px">Item 2<span class="rule"></span><svg class="ic" width="8" height="10" style="color:#c5c9cf"><use href="#trash"/></svg></div>
    <div class="field" style="top:452px"><span class="lab">Item Name</span>Site Cleanup (per hr)</div>
    <div class="field" style="top:501px;width:109px"><span class="lab">Unit Cost</span>$40.00</div>
    <div class="field" style="top:501px;left:125px;width:110px"><span class="lab">Quantity</span>1.5</div>
    <div class="field area" style="top:549px"><span class="lab">Additional Details</span></div>
    <div class="chk off" style="top:645px"><span class="box"></span>Save this item for future use</div>

    <div class="sec" style="top:684px">Item 3<span class="rule"></span><svg class="ic" width="8" height="10" style="color:#c5c9cf"><use href="#trash"/></svg></div>
    <div class="field" style="top:711px"><span class="lab">Item Name</span>Tree Trimming (per hr)</div>
    <div class="field" style="top:759px;width:109px"><span class="lab">Unit Cost</span>$150.00</div>
    <div class="field" style="top:759px;left:125px;width:110px"><span class="lab">Quantity</span>1</div>
    <div class="field area" style="top:808px"><span class="lab">Additional Details</span></div>
    <div class="chk" style="top:904px"><span class="box on"><svg class="ic" width="9" height="9" style="color:var(--green)"><use href="#tick"/></svg></span>Save this item for future use</div>
    <div class="addbtn" style="top:946px"><svg class="ic" width="6" height="6"><use href="#plus"/></svg>ADD ITEM</div>
    <div class="btn" style="top:996px"><svg class="ic" width="10" height="10"><use href="#go"/></svg>NEXT</div>
  </section>

  <!-- POPUP : MY ITEMS -->
  <section class="phone" style="left:651px;top:184px;height:479px">
    <div class="shade-top"></div><div class="shade-bot"></div>
    <div class="status" style="color:#5a6480"><svg class="ic" width="24" height="9"><use href="#signal"/></svg>15:30</div>
    <div class="appbar" style="color:#4a5677"><svg class="ic back" width="14" height="14"><use href="#back"/></svg>Create Estimate<svg class="ic menu" width="4" height="12"><use href="#kebab"/></svg></div>
    <div class="field" style="top:451px;height:28px;background:transparent;border-color:#55585e;color:#6e7279"><span class="lab" style="background:#3c3e43;color:#6e7279">Item Name</span>Site Cleanup (per hr)</div>
    <div class="dialog">
      <span class="close"></span>
      <h3 class="head"><svg class="ic" width="16" height="16"><use href="#house"/></svg>MY ITEMS</h3>
      <div class="opt" style="top:67px;height:52px"><span class="box on"><svg class="ic" width="9" height="9" style="color:var(--green)"><use href="#tick"/></svg></span><span class="nm">Asphalt (per sqft)<small>including labour costs</small></span><span>$85.00</span></div>
      <div class="opt" style="top:119px;height:37px"><span class="box"></span><span class="nm">Lawn Mowing (per hr)</span><span>$50.00</span></div>
      <div class="opt" style="top:156px;height:37px"><span class="box"></span><span class="nm">Monthly Checkup</span><span>$9.95</span></div>
      <div class="opt" style="top:193px;height:37px"><span class="box"></span><span class="nm">Monthly Maintenance</span><span>$39.99</span></div>
      <div class="opt" style="top:230px;height:37px"><span class="box on"><svg class="ic" width="9" height="9" style="color:var(--green)"><use href="#tick"/></svg></span><span class="nm">Site Cleanup (per hr)</span><span>$40.00</span></div>
      <div class="opt last" style="top:267px;height:37px"><span class="box"></span><span class="nm">Tree Removal (per hr)</span><span>$250.00</span></div>
      <div class="btn" style="left:34px;top:322px"><svg class="ic" width="10" height="10"><use href="#go"/></svg>SELECT</div>
    </div>
  </section>

  <!-- STEP 03 : PAYMENT -->
  <section class="phone" style="left:56px;top:1253px;height:975px">
    <div class="hero"></div>
    <div class="status"><svg class="ic" width="24" height="9"><use href="#signal"/></svg>15:30</div>
    <div class="appbar"><svg class="ic back" width="14" height="14"><use href="#back"/></svg>Create Estimate<svg class="ic menu" width="4" height="12"><use href="#kebab"/></svg></div>
    <div class="stepper"><span class="dot done"><svg class="ic" width="10" height="10"><use href="#tick"/></svg></span><span class="dot done"><svg class="ic" width="10" height="10"><use href="#tick"/></svg></span><span class="dot cur">3</span><span class="dot">4</span><span class="dot">5</span></div>
    <div class="tab"></div><div class="card"></div>
    <h2 class="title"><svg class="ic" width="17" height="15"><use href="#wallet"/></svg>PAYMENT</h2>

    <div class="sec" style="top:166px">Discount<span class="rule"></span></div>
    <div class="field" style="top:191px;width:109px;height:33px"><span class="lab">Method</span>Rate (%)<svg class="ic chev" width="9" height="6"><use href="#chev"/></svg></div>
    <div class="field" style="top:191px;left:125px;width:110px;height:33px"><span class="lab">Amount</span>10</div>
    <div class="field area" style="top:241px"><span class="lab">Notes</span>First-time Customer</div>

    <div class="sec" style="top:350px">Tax<span class="rule"></span></div>
    <div class="field" style="top:377px"><span class="lab">Rate (%)</span>6.25%</div>

    <div class="sec" style="top:436px">Shipping<span class="rule"></span></div>
    <div class="field" style="top:462px"><span class="lab">Fee</span><span class="ph">$0.00</span></div>
    <div class="field area" style="top:511px"><span class="lab">Notes</span></div>

    <div class="sec" style="top:621px">Options<span class="rule"></span></div>
    <div class="field" style="top:647px"><span class="lab">Deposit</span><span class="ph">$0.00</span></div>
    <div class="field area" style="top:696px"><span class="lab">Scheduled Payments</span></div>

    <div class="lbl" style="top:796px">Accept Credit Cards</div>
    <div class="toggle on" style="top:796px">ON</div>
    <div class="pays" style="top:815px"><span class="pay">Varda</span><span class="pay">Merix</span><span class="pay">Dovra</span><span class="pay">Amvel</span><span class="pay">Paylo</span></div>
    <div class="lbl" style="top:847px">Accept eCheck</div>
    <div class="toggle off" style="top:847px">OFF</div>
    <div class="pays" style="top:866px"><span class="pay">CHECK</span></div>
    <div class="btn" style="top:910px"><svg class="ic" width="10" height="10"><use href="#go"/></svg>NEXT</div>
  </section>

  <!-- STEP 04 : DOCUMENT INFO -->
  <section class="phone" style="left:364px;top:1253px;height:610px">
    <div class="hero"></div>
    <div class="status"><svg class="ic" width="24" height="9"><use href="#signal"/></svg>15:30</div>
    <div class="appbar"><svg class="ic back" width="14" height="14"><use href="#back"/></svg>Create Estimate<svg class="ic menu" width="4" height="12"><use href="#kebab"/></svg></div>
    <div class="stepper"><span class="dot done"><svg class="ic" width="10" height="10"><use href="#tick"/></svg></span><span class="dot done"><svg class="ic" width="10" height="10"><use href="#tick"/></svg></span><span class="dot done"><svg class="ic" width="10" height="10"><use href="#tick"/></svg></span><span class="dot cur">4</span><span class="dot">5</span></div>
    <div class="tab"></div><div class="card"></div>
    <h2 class="title"><svg class="ic" width="12" height="16"><use href="#doc"/></svg>DOCUMENT INFO.</h2>

    <div class="sec" style="top:166px">Notes<span class="rule"></span></div>
    <div class="field area" style="top:191px;height:140px;line-height:15px;padding-top:9px"><span class="lab">Message for Client</span>Lorem ipsum dolor sit amet, consectetur adipiscing elit. Curabitur sapien ipsum, gravida ac ligula et, tincidunt laoreet tellus. Morbi tincidunt felis quis elit rhoncus lobortis. Integer ac sem sed libero congue.</div>

    <div class="sec" style="top:358px">Photos<span class="rule"></span></div>
    <div class="photo a" style="left:17px;top:379px" role="img" aria-label="Photo of a house front with driveway"><span class="x"></span></div>
    <div class="photo b" style="left:73px;top:379px" role="img" aria-label="Photo of a two-storey house exterior"><span class="x"></span></div>
    <div class="addphoto" style="left:128px;top:379px"><svg class="ic" width="16" height="16" style="color:#c4c8ce"><use href="#plus"/></svg></div>

    <div class="sec" style="top:453px">Signatures<span class="rule"></span></div>
    <div class="lbl" style="top:477px">My Signature</div>
    <div class="toggle off" style="top:477px">OFF</div>
    <div class="lbl" style="top:502px">Client Signature</div>
    <div class="toggle on" style="top:502px">ON</div>
    <div class="btn" style="top:544px"><svg class="ic" width="10" height="10"><use href="#go"/></svg>NEXT</div>
  </section>

  <!-- swipe action row -->
  <div class="swipe">
    <span style="left:3px;top:19px">(6.25%)</span>
    <span style="left:137px;top:19px">$59.62</span>
    <span style="left:185px;top:0;width:32px;height:48px;background:#fdecec;display:flex;align-items:center;justify-content:center;color:var(--red)"><svg class="ic" width="9" height="11"><use href="#trash"/></svg></span>
    <span style="left:219px;top:0;width:33px;height:48px;background:#eef7e3;display:flex;align-items:center;justify-content:center;color:var(--green)"><svg class="ic" width="11" height="11"><use href="#pencil"/></svg></span>
  </div>

  <!-- STEP 05 : ESTIMATE -->
  <section class="phone" style="left:672px;top:1253px;height:1238px">
    <div class="hero"></div>
    <div class="status"><svg class="ic" width="24" height="9"><use href="#signal"/></svg>15:30</div>
    <div class="appbar"><svg class="ic back" width="14" height="14"><use href="#back"/></svg>Create Estimate<svg class="ic menu" width="4" height="12"><use href="#kebab"/></svg></div>
    <div class="stepper"><span class="dot done"><svg class="ic" width="10" height="10"><use href="#tick"/></svg></span><span class="dot done"><svg class="ic" width="10" height="10"><use href="#tick"/></svg></span><span class="dot done"><svg class="ic" width="10" height="10"><use href="#tick"/></svg></span><span class="dot done"><svg class="ic" width="10" height="10"><use href="#tick"/></svg></span><span class="dot cur">5</span></div>
    <div class="tab"></div><div class="card"></div>
    <h2 class="title"><svg class="ic" width="18" height="16"><use href="#eye"/></svg>ESTIMATE</h2>

    <svg class="ic pen" width="11" height="11" style="top:166px;color:var(--green)"><use href="#pencil"/></svg>
    <div class="logo">MY LOGO</div>
    <p class="ctr" style="top:231px;font-weight:700;font-size:8.5px">My Company</p>
    <p class="ctr" style="top:244px">77 Quarry Road, Halden, TX 76999</p>
    <p class="ctr" style="top:256px">555.642.1190 &nbsp;|&nbsp; info@mycompany.example</p>
    <p class="ctr" style="top:268px">www.mycompany.example</p>
    <div style="left:108px;top:295px;width:36px;height:1px;background:#c8ccd2"></div>
    <p class="ctr" style="top:312px"><b>Estimate #:</b> MOB00001</p>
    <p class="ctr" style="top:327px"><b>Created on:</b> 05/08/2019</p>

    <div class="sh" style="top:347px"><svg class="ic" width="10" height="10"><use href="#person"/></svg>TO<svg class="ic last" width="10" height="10" style="color:var(--green)"><use href="#pencil"/></svg></div>
    <div class="row" style="top:371px"><b>Pellwick Diner</b></div>
    <div class="row sub" style="top:387px">48 Alder Lane</div>
    <div class="row sub" style="top:399px">Brookvale, TX 75999</div>
    <div class="row sub" style="top:413px">info@pellwickdiner.example</div>
    <div class="row sub" style="top:427px;justify-content:flex-start">m: 555.201.3344 &nbsp;|&nbsp; p: 555.310.7781</div>

    <div class="sh" style="top:463px"><svg class="ic" width="10" height="10"><use href="#house"/></svg>JOB DESCRIPTION<svg class="ic last" width="10" height="10" style="color:var(--green)"><use href="#pencil"/></svg></div>
    <div class="row" style="top:490px"><b>Asphalt (per sqft)</b><span>$850.00</span></div>
    <div class="row sub" style="top:506px"><span>including labour costs</span><span>$85.00 X 10</span></div>
    <div class="sep" style="top:526px"></div>
    <div class="row" style="top:537px"><b>Site Cleanup (per hr)</b><span>$60.00</span></div>
    <div class="row sub" style="top:553px"><span></span><span>$40.00 X 1.5</span></div>
    <div class="sep" style="top:573px"></div>
    <div class="row" style="top:584px"><b>Tree Trimming (per hr)</b><span>$150.00</span></div>
    <div class="row sub" style="top:600px"><span></span><span>$150.00 X 1</span></div>
    <div class="sep" style="top:620px"></div>
    <div class="row ind" style="top:631px"><b>Subtotal</b><span>$1060.00</span></div>
    <div class="sep ind" style="top:652px"></div>
    <div class="row ind" style="top:662px"><span><b>Discount</b> (10%)</span><span>-$106.00</span></div>
    <div class="row ind sub" style="top:676px">First-time Customer</div>
    <div class="sep ind" style="top:696px"></div>
    <div class="row ind" style="top:706px"><span><b>Tax</b> (6.25%)</span><span>$59.62</span></div>
    <div class="sep ind" style="top:727px"></div>
    <div class="row ind" style="top:737px"><b>TOTAL</b><b>$1013.62</b></div>

    <div class="sh" style="top:785px"><svg class="ic" width="10" height="9"><use href="#wallet"/></svg>PAYMENT<svg class="ic last" width="10" height="10" style="color:var(--green)"><use href="#pencil"/></svg></div>
    <div class="row sub" style="top:809px">We accept:</div>
    <div class="pays" style="top:827px"><span class="pay">Varda</span><span class="pay">Merix</span><span class="pay">Dovra</span><span class="pay">Amvel</span><span class="pay">Paylo</span></div>

    <div class="sh" style="top:869px"><svg class="ic" width="8" height="10"><use href="#doc"/></svg>ADDITIONAL INFO.<svg class="ic last" width="10" height="10" style="color:var(--green)"><use href="#pencil"/></svg></div>
    <p class="para" style="top:891px">Lorem ipsum dolor sit amet, consectetur adipiscing elit. Curabitur sapien ipsum, gravida ac ligula et, tincidunt laoreet tellus. Morbi tincidunt felis quis elit rhoncus lobortis. Integer ac sem sed libero congue.</p>
    <div class="photo a" style="left:17px;top:955px" role="img" aria-label="Photo of a house front with driveway"></div>
    <div class="photo b" style="left:67px;top:955px" role="img" aria-label="Photo of a two-storey house exterior"></div>

    <div class="sh" style="top:1026px"><svg class="ic" width="10" height="10"><use href="#okcircle"/></svg>ACCEPTANCE<svg class="ic last" width="10" height="10" style="color:var(--green)"><use href="#pencil"/></svg></div>
    <p class="para" style="top:1049px">The above prices,specifications, and conditions are satisfactory and are hereby accepted.</p>
    <p class="para" style="top:1080px;color:var(--orange);font-weight:700;left:17px">Approved by (Client Signature)</p>
    <div class="sigbox" style="top:1098px"></div>
    <div class="btn go" style="top:1172px"><svg class="ic" width="10" height="10"><use href="#go"/></svg>SEND TO CLIENT</div>
  </section>

</main>
</body>
</html>
```